Homepage Real Estate Agency

I need a web design for a real estate agency in Luxembourg. A short draft for the front page can be found in the project details. (Page 1+2) The main colors of the site should be blue as shown in the project details. (Page 3)
The main target for this site is to promote real estates and a small presentation of the company.

Industry/Entity Type

Real Estate

Requirements
Must have
• On the front page estates are shown in a short preview in small boxes, on the right side is a search. The search is hidden except for the front page. The header has 4 buttons and the logo of the company.

```html
<!DOCTYPE html>
<html lang="fr">
<head>
<meta charset="utf-8">
<title>Maison Lumen – Immobilier</title>
<link rel="stylesheet" href="https://fonts.googleapis.com/css2?family=Oswald:wght@500&family=Pathway+Gothic+One&family=PT+Sans:ital,wght@0,400;1,400&family=Didact+Gothic&display=swap">
<style>
  :root {
    --page-bg: #f1f1f1;
    --blue: #1f73b7;
    --blue-light: #3d92d4;
    --blue-dark: #125a99;
    --heading-blue: #2a74b4;
    --text: #1e1e1e;
    --muted: #555;
    --rule: #d4d4d4;
    --white: #ffffff;
    --dark-btn: #2e2e2e;
  }
  * { box-sizing: border-box; margin: 0; padding: 0; }
  html, body { width: 1076px; height: 1200px; overflow: hidden; }
  body {
    position: relative;
    background: var(--page-bg);
    font-family: "PT Sans", sans-serif;
    color: var(--text);
  }
  .abs { position: absolute; }

  /* Header */
  .brand-tab {
    left: 108px; top: 0; width: 191px; height: 183px;
    background: linear-gradient(#d6d6d6, #e9e9e9);
    border: 1px solid #2a6fb0; border-top: none;
    border-radius: 0 0 96px 96px;
    display: flex; flex-direction: column; align-items: center; justify-content: center;
    padding-bottom: 30px; gap: 8px;
  }
  .brand-dot { width: 22px; height: 22px; border-radius: 50%; background: var(--blue); }
  .brand-name {
    font-family: "Oswald", sans-serif; font-weight: 500; font-size: 22px;
    color: var(--blue); letter-spacing: 0.5px;
  }
  .main-nav {
    left: 364px; top: 58px; width: 693px; height: 80px;
    background: linear-gradient(var(--blue-light), var(--blue) 55%, var(--blue-dark));
    border-radius: 10px;
    box-shadow: 0 12px 14px -8px rgba(0,0,0,0.35);
    display: flex;
  }
  .main-nav a {
    display: flex; align-items: center; justify-content: center;
    font-family: "Oswald", sans-serif; font-weight: 500; font-size: 21px;
    color: var(--white); text-decoration: none;
    border-right: 1px solid rgba(255,255,255,0.3);
  }
  .main-nav a:last-child { border-right: none; }

  /* Slider */
  .slide { background: var(--white); box-shadow: 0 3px 8px rgba(0,0,0,0.35); padding: 7px; }
  .slide .photo { width: 100%; height: 100%; }
  .slide-left { left: 54px; top: 247px; width: 228px; height: 221px; }
  .slide-right { left: 796px; top: 247px; width: 226px; height: 223px; }
  .slide-center { left: 280px; top: 205px; width: 521px; height: 296px; padding: 8px; }
  .photo-a { background: linear-gradient(#8fb6de, #b6745e 45%, #4f6b3a); }
  .photo-b { background: linear-gradient(#5f8fc4, #6f7d63 45%, #4b6a3a 85%, #8aa85a); }
  .photo-c { background: linear-gradient(#7aa9da, #d8d6d0 45%, #5f9a3e); }
  .slider-arrow { top: 338px; }

  .h-rule { left: 19px; width: 1033px; height: 1px; background: var(--rule); }

  /* Listings */
  .section-title {
    font-family: "Pathway Gothic One", sans-serif; font-style: italic;
    font-size: 27px; color: var(--heading-blue); font-weight: 400;
  }
  .listing {
    top: 599px; width: 230px; height: 297px;
    background: var(--white); padding: 8px;
  }
  .listing .thumb { height: 144px; }
  .thumb-1 { background: linear-gradient(#6d94c4, #b69e7e 50%, #4a6a33); }
  .thumb-2 { background: linear-gradient(#8db6e0, #7f97ab 50%, #5b7a3c); }
  .thumb-3 { background: linear-gradient(#a9c6e6, #e7e7e4 50%, #5f9a3c); }
  .listing h3 {
    font-family: "Pathway Gothic One", sans-serif; font-weight: 400;
    font-size: 25px; color: #333; margin: 12px 0 0 2px;
  }
  .listing p {
    font-style: italic; font-size: 12px; line-height: 14.5px;
    text-align: justify; margin: 10px 2px 0;
  }
  .review-btn {
    top: 876px; width: 152px; height: 41px; border-radius: 21px;
    background: linear-gradient(var(--blue-light), var(--blue-dark));
    box-shadow: 0 2px 4px rgba(0,0,0,0.3);
    color: var(--white); font-family: "Pathway Gothic One", sans-serif;
    font-size: 21px; display: flex; align-items: center; justify-content: center;
  }
  .pager { left: 635px; top: 941px; display: flex; align-items: center; gap: 7px; font-style: italic; font-size: 14px; }
  .pager span.label { margin-right: 6px; }
  .pager .page-num {
    width: 26px; height: 27px; border: 1px solid #222; background: var(--white);
    display: flex; align-items: center; justify-content: center; font-style: italic;
  }
  .intro {
    left: 30px; top: 1012px; width: 732px;
    font-size: 13.4px; line-height: 17px; text-align: justify;
  }

  /* Search */
  .v-rule { left: 775px; top: 551px; width: 1px; height: 530px; background: var(--rule); }
  .search-title { left: 797px; width: 228px; top: 545px; text-align: center; }
  .field-label { left: 797px; font-family: "Didact Gothic", sans-serif; font-size: 13.5px; color: #222; }
  .field { background: var(--white); border: 1px solid #9a9a9a; height: 27px; }
  .field-wide { left: 805px; width: 239px; }
  .field-small { width: 74px; }
  .search-btn {
    left: 855px; top: 982px; width: 139px; height: 41px; border-radius: 12px;
    background: var(--dark-btn); color: var(--white);
    font-family: "Didact Gothic", sans-serif; font-size: 23px;
    display: flex; align-items: center; justify-content: center;
  }

  /* Footer */
  .footer-nav { top: 1136px; left: 0; width: 1076px; font-size: 13.5px; }
  .footer-nav span { position: absolute; }
  .copyright { top: 1168px; left: 0; width: 1076px; text-align: center; font-size: 13.5px; }
</style>
</head>
<body>
  <header>
    <div class="abs brand-tab">
      <span class="brand-dot"></span>
      <span class="brand-name">Maison Lumen</span>
    </div>
    <nav class="abs main-nav">
      <a href="#" style="width:161px">A Vendre</a>
      <a href="#" style="width:191px">Construction</a>
      <a href="#" style="width:160px">Location</a>
      <a href="#" style="width:181px">Cherchons</a>
    </nav>
  </header>

  <section class="featured-slider">
    <div class="abs slide slide-left"><div class="photo photo-a" role="img" aria-label="Photo of a half-timbered cottage with garden"></div></div>
    <div class="abs slide slide-right"><div class="photo photo-c" role="img" aria-label="Photo of a white suburban house with lawn"></div></div>
    <div class="abs slide slide-center"><div class="photo photo-b" role="img" aria-label="Photo of a craftsman-style house with front garden"></div></div>
    <svg class="abs slider-arrow" style="left:13px" width="30" height="30" viewBox="0 0 30 30" aria-label="Previous">
      <circle cx="15" cy="15" r="14" fill="#9a9a9a" stroke="#777"/>
      <circle cx="15" cy="15" r="11" fill="#c9c9c9"/>
      <path d="M17 10 L11 15 L17 20 Z" fill="#333"/>
    </svg>
    <svg class="abs slider-arrow" style="left:1031px" width="30" height="30" viewBox="0 0 30 30" aria-label="Next">
      <circle cx="15" cy="15" r="14" fill="#9a9a9a" stroke="#777"/>
      <circle cx="15" cy="15" r="11" fill="#c9c9c9"/>
      <path d="M13 10 L19 15 L13 20 Z" fill="#333"/>
    </svg>
  </section>

  <div class="abs h-rule" style="top:529px"></div>

  <main>
    <h2 class="abs section-title" style="left:30px; top:549px">Find the House of your Dream.....</h2>

    <article class="abs listing" style="left:28px">
      <div class="thumb thumb-1" role="img" aria-label="Photo of a large family house"></div>
      <h3>Lorem Ipsum..</h3>
      <p>Lorem ipsum dolor sit amet, consectetur adipisicing elit, sed do eiusmod tempor incididunt ut labore et dolore magna aliqua.</p>
    </article>
    <article class="abs listing" style="left:275px">
      <div class="thumb thumb-2" role="img" aria-label="Photo of a blue two-storey house with porch"></div>
      <h3>Lorem Ipsum..</h3>
      <p>Lorem ipsum dolor sit amet, consectetur adipisicing elit, sed do eiusmod tempor incididunt ut labore et dolore magna aliqua.</p>
    </article>
    <article class="abs listing" style="left:523px">
      <div class="thumb thumb-3" role="img" aria-label="Photo of a white farmhouse on a lawn"></div>
      <h3>Lorem Ipsum..</h3>
      <p>Lorem ipsum dolor sit amet, consectetur adipisicing elit, sed do eiusmod tempor incididunt ut labore et dolore magna aliqua.</p>
    </article>

    <a class="abs review-btn" style="left:69px">View Full Review</a>
    <a class="abs review-btn" style="left:316px">View Full Review</a>
    <a class="abs review-btn" style="left:564px">View Full Review</a>

    <div class="abs pager">
      <span class="label">Page :</span>
      <span class="page-num">1</span>
      <span class="page-num">2</span>
    </div>

    <h2 class="abs section-title" style="left:30px; top:960px">Find the right Realtor</h2>
    <p class="abs intro">Lorem ipsum dolor sit amet, consectetur adipisicing elit, sed do eiusmod tempor incididunt ut labore et dolore magna aliqua. Ut enim ad minim veniam, quis nostrud exercitation ullamco laboris nisi ut aliquip ex ea commodo consequat. Duis aute irure dolor in reprehenderit in voluptate velit esse cillum dolore eu fugiat nulla pariatur. Excepteur sint occaecat cupidatat non proident, sunt in culpa qui officia deserunt mollit anim id est laborum.</p>
  </main>

  <div class="abs v-rule"></div>

  <aside class="property-search">
    <h2 class="abs section-title search-title">Find a Property</h2>
    <span class="abs field-label" style="top:597px">Category :</span>
    <div class="abs field field-wide" style="top:621px"></div>
    <span class="abs field-label" style="top:661px">City or State :</span>
    <div class="abs field field-wide" style="top:685px"></div>
    <span class="abs field-label" style="top:726px">Area Range :</span>
    <div class="abs field field-small" style="left:805px; top:750px"></div>
    <div class="abs field field-small" style="left:945px; top:750px"></div>
    <span class="abs field-label" style="top:791px">Price Range :</span>
    <div class="abs field field-small" style="left:805px; top:815px"></div>
    <div class="abs field field-small" style="left:945px; top:815px"></div>
    <span class="abs field-label" style="top:855px">Beds :</span>
    <div class="abs field field-small" style="left:805px; top:879px"></div>
    <span class="abs field-label" style="top:920px">Baths :</span>
    <div class="abs field field-small" style="left:805px; top:944px"></div>
    <a class="abs search-btn">Search</a>
  </aside>

  <div class="abs h-rule" style="top:1108px"></div>

  <footer>
    <div class="abs footer-nav">
      <span style="left:326px">Home</span>
      <span style="left:396px">|</span>
      <span style="left:434px">About Us</span>
      <span style="left:525px">|</span>
      <span style="left:562px">Projects</span>
      <span style="left:646px">|</span>
      <span style="left:682px">Contact Us</span>
    </div>
    <p class="abs copyright">Copyright 2012. All Rights Reserved.</p>
  </footer>
</body>
</html>
```